Simple and clean webdesign for personal homepage

Trying to create a simple and clean webdesign for my personal homepage. Going to use a static site builder with templates to build the site. I want it to have multiple pages - like an about me, blog and resume. I just need something very basic I can customize. I want the main colors to be purple, black and white. I am open to other color palettes too but since purple is my favorite color I want that to be one of the main colors.

The site be mostly text driven. Might have some images in the body text but I want the site design to be light and lean.

Industry/Entity Type

Personal Homepage.

Coding

Coded - Design and coding required

Number of Pages Required

1 page

Font styles to use
Sans Serif

Colors
6B429C
8869AF
B7A5CE
E3DAEB
F3F0F8

Requirements
Must have
• Clean design. Purple used as a color. HTML template.
Nice to have
• Responsive

```html
<!DOCTYPE html>
<html lang="en">
<head>
<meta charset="utf-8">
<title>Daniel Hart — Blog</title>
<link rel="stylesheet" href="https://fonts.googleapis.com/css2?family=Poppins:wght@400;500;600;700&display=swap">
<style>
:root{
  --purple:#6B429C;
  --purple-mid:#8869AF;
  --purple-soft:#B7A5CE;
  --lavender:#E3DAEB;
  --lavender-pale:#F3F0F8;
  --ink:#1d1d1f;
  --text:#555;
  --line:#e4e0ea;
  --white:#fff;
}
*{box-sizing:border-box;margin:0;padding:0}
html,body{width:733px;height:1200px;overflow:hidden}
body{font-family:"Poppins",Arial,sans-serif;color:var(--text);background:var(--white);position:relative;font-size:7px;line-height:1.5}
.site-header{height:48px;display:flex;align-items:center;padding:0 34px 0 85px;background:var(--white)}
.brand{font-size:19px;font-weight:700;color:var(--purple);letter-spacing:1px;width:240px}
.main-nav{display:flex;gap:14px;font-size:8px;font-weight:500;color:var(--ink);flex:1}
.main-nav .active{color:var(--purple)}
.header-phone{display:flex;align-items:center;gap:5px;font-size:13px;font-weight:500;color:var(--purple)}
.header-phone svg{width:15px;height:15px}
.hero{height:142px;background:linear-gradient(180deg,var(--lavender-pale),var(--lavender));text-align:center;padding-top:52px;position:relative}
.hero h1{font-size:21px;font-weight:600;color:var(--purple)}
.hero p{width:420px;margin:4px auto 0;font-size:7px;color:var(--text)}
.social-rail{position:absolute;left:28px;top:36px;display:flex;flex-direction:column;gap:6px}
.social-rail span{width:13px;height:13px;border:1px solid var(--purple-mid);background:var(--white)}
.content{display:flex;padding:18px 0 0 85px;gap:20px;height:610px;position:relative}
.posts{width:362px}
.post{display:flex;gap:8px;height:110px}
.post-thumb{width:125px;height:92px;background:linear-gradient(135deg,#7b8796,#c7ccd3 60%,#e9e2d6)}
.post-meta{font-size:6.5px;color:var(--ink);margin-top:2px}
.post h2{font-size:9px;font-weight:600;color:var(--purple);margin:1px 0 3px}
.post p{font-size:6.5px;line-height:1.45}
.read-more{display:inline-block;margin-top:4px;font-size:6.5px;color:var(--purple);border-bottom:1px solid var(--purple)}
.to-top{position:absolute;left:455px;top:88px;width:15px;height:15px;background:var(--ink)}
.sidebar{width:180px;padding-top:2px}
.widget{border:1px solid var(--line);box-shadow:0 2px 6px rgba(107,66,156,.12);padding:10px;margin-bottom:12px}
.widget h3{font-size:9px;font-weight:600;color:var(--purple);padding-bottom:4px;border-bottom:1px solid var(--line);margin-bottom:6px}
.widget input{display:block;width:100%;height:17px;border:1px solid var(--line);font:inherit;font-size:6.5px;padding:0 5px;margin:6px 0}
.btn-dark{background:var(--ink);color:var(--white);font-size:6.5px;padding:4px 7px;border:0;font-family:inherit}
.icons{display:flex;gap:5px}
.icons span{width:13px;height:13px;border:1px solid var(--purple-mid)}
.tags{display:flex;flex-wrap:wrap;gap:4px 6px;font-size:6px}
.watermark-name{font-size:15px;font-weight:700;letter-spacing:2px;color:var(--lavender);text-align:center;margin-top:38px}
.pagination{position:absolute;left:85px;width:362px;top:578px;display:flex;justify-content:center;gap:4px;font-size:6.5px}
.pagination span{width:11px;height:11px;border:1px solid var(--purple-soft);display:flex;align-items:center;justify-content:center;color:var(--purple)}
.pagination .current{border-radius:50%;background:var(--purple);color:var(--white)}
.contact{height:400px;background:linear-gradient(180deg,var(--white),var(--lavender-pale));text-align:center;padding-top:30px}
.contact h2{font-size:21px;font-weight:600;color:var(--purple)}
.contact .lead{width:420px;margin:4px auto 0;font-size:7px}
.contact-grid{display:flex;gap:12px;margin:18px 0 0 85px;text-align:left}
.info-cards{width:150px;display:flex;flex-direction:column;gap:9px}
.info-card{background:var(--white);box-shadow:0 2px 6px rgba(107,66,156,.14);display:flex;gap:8px;padding:8px;height:44px}
.info-card svg{width:12px;height:12px;flex:none;margin-top:1px}
.info-card b{display:block;font-size:8px;color:var(--ink);font-weight:600}
.info-card span{font-size:6px}
.contact-form{width:406px;display:grid;grid-template-columns:1fr 1fr;gap:9px}
.field{background:var(--white);height:22px;box-shadow:0 2px 6px rgba(107,66,156,.12);display:flex;align-items:center;gap:5px;padding:0 8px;font-size:6.5px;color:#888}
.field svg{width:8px;height:8px}
.field.message{grid-column:1/3;height:62px;align-items:flex-start;padding-top:7px}
.btn-submit{grid-column:2;justify-self:end;background:var(--purple);color:var(--white);border:0;border-radius:12px;font-family:inherit;font-size:7px;padding:6px 13px}
.site-footer{position:absolute;left:0;bottom:0;width:733px;height:30px;background:var(--purple);color:var(--white);display:flex;align-items:center;padding:0 34px 0 85px;font-size:6.5px}
.site-footer .follow{margin-left:auto;display:flex;align-items:center;gap:5px;font-size:8px}
.site-footer .follow span{width:12px;height:12px;border:1px solid var(--white)}
</style>
</head>
<body>
<header class="site-header">
  <div class="brand">DANIEL HART</div>
  <nav class="main-nav"><span>About Me</span><span class="active">Blog</span><span>Resume</span><span>Contact Me</span></nav>
  <div class="header-phone">
    <svg viewBox="0 0 24 24" fill="none" stroke="currentColor" stroke-width="2"><path d="M6 3h4l2 5-3 2a11 11 0 0 0 5 5l2-3 5 2v4a2 2 0 0 1-2 2A17 17 0 0 1 4 5a2 2 0 0 1 2-2z"/></svg>
    555.010.2468
  </div>
</header>

<section class="hero">
  <div class="social-rail" aria-label="Social links"><span></span><span></span><span></span></div>
  <h1>My Blog Posts</h1>
  <p>Short notes on writing, design and daily work, gathered here to read at your own pace. New posts arrive each week with fresh ideas and simple tips.</p>
</section>

<main class="content">
  <div class="posts">
    <article class="post"><div class="post-thumb" role="img" aria-label="Photo of a laptop on a desk"></div><div><div class="post-meta">▣ April 16th, 2020</div><h2>Lorem Ipsum Dolor Sit Amet</h2><p>Short post summary about a recent idea, written plainly so the reader knows what the full article covers before opening it.</p><span class="read-more">Read More</span></div></article>
    <article class="post"><div class="post-thumb" role="img" aria-label="Photo of a man working at a laptop"></div><div><div class="post-meta">▣ April 16th, 2020</div><h2>Lorem Ipsum Dolor Sit Amet</h2><p>Short post summary about a recent idea, written plainly so the reader knows what the full article covers before opening it.</p><span class="read-more">Read More</span></div></article>
    <article class="post"><div class="post-thumb" role="img" aria-label="Photo of a business meeting"></div><div><div class="post-meta">▣ April 16th, 2020</div><h2>Lorem Ipsum Dolor Sit Amet</h2><p>Short post summary about a recent idea, written plainly so the reader knows what the full article covers before opening it.</p><span class="read-more">Read More</span></div></article>
    <article class="post"><div class="post-thumb" role="img" aria-label="Photo of a person by a bright window"></div><div><div class="post-meta">▣ April 16th, 2020</div><h2>Lorem Ipsum Dolor Sit Amet</h2><p>Short post summary about a recent idea, written plainly so the reader knows what the full article covers before opening it.</p><span class="read-more">Read More</span></div></article>
    <article class="post"><div class="post-thumb" role="img" aria-label="Photo of a team around a table"></div><div><div class="post-meta">▣ April 16th, 2020</div><h2>Lorem Ipsum Dolor Sit Amet</h2><p>Short post summary about a recent idea, written plainly so the reader knows what the full article covers before opening it.</p><span class="read-more">Read More</span></div></article>
  </div>
  <span class="to-top" aria-hidden="true"></span>
  <aside class="sidebar">
    <div class="widget"><h3>Subscribe To Our Blog</h3><p>Get the latest posts and updates sent straight to your inbox.</p><input placeholder="Enter your email"><button class="btn-dark">Subscribe</button></div>
    <div class="widget"><h3>Follow Me On</h3><div class="icons"><span></span><span></span><span></span></div></div>
    <div class="widget"><h3>Tags</h3><div class="tags"><span>Permalink</span><span>DropMenu</span><span>Gallery</span><span>Template</span><span>Permalink</span><span>DropMenu</span><span>Gallery</span><span>Template</span><span>Permalink</span><span>DropMenu</span><span>Gallery</span><span>Template</span><span>Permalink</span><span>DropMenu</span><span>Gallery</span></div></div>
    <div class="watermark-name">DANIEL HART</div>
  </aside>
  <nav class="pagination"><span>‹</span><span class="current">1</span><span>2</span><span>3</span><span>›</span></nav>
</main>

<section class="contact">
  <h2>Contact Me Today</h2>
  <p class="lead">Have a question or an idea to share? Send a message using the form below and I will reply as soon as I can, usually within two days.</p>
  <div class="contact-grid">
    <div class="info-cards">
      <div class="info-card"><svg viewBox="0 0 24 24" fill="#6B429C"><path d="M12 2a7 7 0 0 0-7 7c0 5 7 13 7 13s7-8 7-13a7 7 0 0 0-7-7zm0 9.5A2.5 2.5 0 1 1 12 6.5a2.5 2.5 0 0 1 0 5z"/></svg><div><b>Address</b><span>Street Name, City Name<br>Area Zipcode</span></div></div>
      <div class="info-card"><svg viewBox="0 0 24 24" fill="#6B429C"><path d="M6 3h4l2 5-3 2a11 11 0 0 0 5 5l2-3 5 2v4a2 2 0 0 1-2 2A17 17 0 0 1 4 5a2 2 0 0 1 2-2z"/></svg><div><b>Phone</b><span>+1 555.010.2468</span></div></div>
      <div class="info-card"><svg viewBox="0 0 24 24" fill="#6B429C"><path d="M3 5h18v14H3z" fill="none" stroke="#6B429C" stroke-width="2"/><path d="M3 6l9 7 9-7" fill="none" stroke="#6B429C" stroke-width="2"/></svg><div><b>Email</b><span>info@danielhart.com</span></div></div>
    </div>
    <form class="contact-form">
      <div class="field"><svg viewBox="0 0 10 10"><circle cx="5" cy="3" r="2" fill="#8869AF"/><path d="M1 10a4 4 0 0 1 8 0z" fill="#8869AF"/></svg>Your Name*</div>
      <div class="field"><svg viewBox="0 0 10 10"><rect x="1" y="2" width="8" height="6" fill="#8869AF"/></svg>Your Email*</div>
      <div class="field"><svg viewBox="0 0 10 10"><circle cx="5" cy="5" r="4" fill="#8869AF"/></svg>Your Phone*</div>
      <div class="field"><svg viewBox="0 0 10 10"><rect x="1" y="1" width="8" height="8" fill="#8869AF"/></svg>Subject*</div>
      <div class="field message"><svg viewBox="0 0 10 10"><path d="M1 8l6-6 2 2-6 6H1z" fill="#8869AF"/></svg>Your Message*</div>
      <button class="btn-submit" type="button">Submit Now</button>
    </form>
  </div>
</section>

<footer class="site-footer">
  <span>Copyright © 2022 Daniel Hart. All Rights Reserved.</span>
  <div class="follow">Follow Me On <span></span><span></span><span></span></div>
</footer>
</body>
</html>
```